Electrical panel service sticker w Bucket truck & Logo

We have a rather plain sticker we put on lighting panels to remind customers who to call for service. We want to redesign them with brushed aluminum background. We want a remake of the sticker with the outline of a bucket truck. You'll need to find or draw the outling of a bucket truck maybe with the boom up slightly as we will get these stickers die cut.

We want LOGO with Ph.# and Email.
Electrical * Lighting * Sign Service

Target Market(s)

Commercial property managers

Industry/Entity Type

Property Management

Requirements
Must have
• Bucket Truck Outline

```html
<!DOCTYPE html>
<html lang="en">
<head>
<meta charset="utf-8">
<title>Lumencrest Field Service – Panel Service Sticker</title>
<link rel="stylesheet" href="https://fonts.googleapis.com/css2?family=Archivo:wdth,wght@62..125,700..900&display=swap">
<style>
  :root {
    --page: #ffffff;
    --alu-light: #f4f4f4;
    --alu-mid: #d9d9d9;
    --alu-dark: #bdbdbd;
    --ink: #111111;
    --brand-red: #d9414b;
    --navy: #1f2f5c;
    --white: #ffffff;
  }
  * { box-sizing: border-box; margin: 0; padding: 0; }
  html, body { width: 1200px; height: 900px; overflow: hidden; background: var(--page); }
  .sticker { position: relative; width: 1200px; height: 900px; font-family: "Archivo", Arial, sans-serif; }
  .sticker-shape { position: absolute; inset: 0; }
  .truck-illustration {
    position: absolute; left: 318px; top: 62px; width: 536px; height: 306px;
    border-radius: 14px;
    background: linear-gradient(180deg, #e2e2e2 0%, #c9c9c9 100%);
  }
  .line { position: absolute; left: 0; width: 1200px; text-align: center; white-space: nowrap; }
  .brand-name {
    color: var(--brand-red); font-weight: 900; font-stretch: 125%; line-height: 1;
  }
  .brand-top { top: 384px; font-size: 124px; letter-spacing: 2px; }
  .brand-bottom { top: 510px; font-size: 82px; letter-spacing: 1px; }
  .brand-suffix-row {
    position: absolute; top: 602px; left: 70px; width: 1060px;
    display: flex; align-items: center; gap: 22px;
  }
  .rule { flex: 1; height: 4px; background: var(--brand-red); }
  .brand-suffix { color: var(--brand-red); font-weight: 900; font-stretch: 125%; font-size: 26px; letter-spacing: 2px; line-height: 1; }
  .phone { top: 644px; font-size: 90px; font-weight: 900; font-stretch: 125%; color: var(--ink); line-height: 1; letter-spacing: 2px; }
  .email { top: 727px; font-size: 30px; font-weight: 700; font-stretch: 125%; color: var(--navy); line-height: 1; letter-spacing: 1px; }
  .service-bar {
    position: absolute; left: 58px; top: 776px; width: 1088px; height: 60px;
    background: var(--ink); border-radius: 30px;
    display: flex; align-items: center; justify-content: center; gap: 22px;
    color: var(--white); font-weight: 800; font-stretch: 90%; font-size: 46px; line-height: 1;
  }
  .dot { width: 13px; height: 13px; border-radius: 50%; background: var(--brand-red); }
</style>
</head>
<body>
<main class="sticker">
  <svg class="sticker-shape" width="1200" height="900" viewBox="0 0 1200 900" aria-hidden="true">
    <defs>
      <linearGradient id="brushed-aluminum" x1="0" y1="0" x2="1" y2="1">
        <stop offset="0" stop-color="var(--alu-mid)"/>
        <stop offset="0.35" stop-color="var(--alu-light)"/>
        <stop offset="0.7" stop-color="var(--alu-mid)"/>
        <stop offset="1" stop-color="var(--alu-dark)"/>
      </linearGradient>
    </defs>
    <path class="die-cut" fill="url(#brushed-aluminum)" stroke="#9a9a9a" stroke-width="2"
      d="M40 334 H205 C230 150 400 26 604 26 C808 26 978 150 1002 334 H1160 Q1194 334 1194 368 V856 Q1194 890 1160 890 H40 Q6 890 6 856 V368 Q6 334 40 334 Z"/>
    <path class="inner-border" fill="none" stroke="var(--ink)" stroke-width="7"
      d="M52 356 H222 C248 180 410 50 604 50 C798 50 960 180 986 356 H1148 Q1170 356 1170 378 V846 Q1170 868 1148 868 H52 Q30 868 30 846 V378 Q30 356 52 356 Z"/>
  </svg>

  <div class="truck-illustration" role="img" aria-label="Outline drawing of a utility bucket truck with its boom raised"></div>

  <h1 class="line brand-name brand-top">LUMENCREST</h1>
  <p class="line brand-name brand-bottom">FIELD SERVICE</p>
  <div class="brand-suffix-row">
    <span class="rule"></span>
    <span class="brand-suffix">INCORPORATED</span>
    <span class="rule"></span>
  </div>

  <p class="line phone">877-555-0148</p>
  <p class="line email">SERVICE@LUMENCRESTFIELD.COM</p>

  <div class="service-bar">
    <span>ELECTRICAL</span><span class="dot"></span>
    <span>LIGHTING</span><span class="dot"></span>
    <span>SIGN SERVICE</span>
  </div>
</main>
</body>
</html>
```